Business Card Design

We are a contracting firm, 95% of my work is interior renovations.... but also don't want to preclude the idea of doing exterior work if it arises. I Need a business card that says I am the ultimate professional. There is a per-determined notion that all contractors are shady, unreliable, etc. Being that most of my work is in Manhattan, I would like to give the impression of fresh, modern, sleek, design/build firm.

Target Market(s)

young couples 25-40

Industry/Entity Type

Business

Contact Information for Business Card

PeterHollowayInteriors LLC
27 North Brandel Street
Marsh Hollow NY 11492
718-555-0142
646-555-0187- cell
www.phbwx.com
ph@phbwx.com
Peter Holloway

Requirements
Should not have
• do not want to give the impression of a "bargain basement store"

```html
<!DOCTYPE html>
<html lang="en">
<head>
<meta charset="utf-8">
<title>Peter Holloway Interiors – Business Card</title>
<link rel="stylesheet" href="https://fonts.googleapis.com/css2?family=Exo+2:wght@400;500;600&display=swap">
<style>
  :root {
    --backdrop: #8e8e8e;
    --card-white: #f7f7f5;
    --card-black: #1c1c1c;
    --gold: #e2b321;
    --gold-deep: #c9980f;
    --ink: #2a2a2a;
    --ink-soft: #555;
  }
  * { margin: 0; padding: 0; box-sizing: border-box; }
  html, body { width: 1200px; height: 894px; overflow: hidden; }
  body {
    background: var(--backdrop);
    font-family: "Exo 2", sans-serif;
    position: relative;
  }
  .card {
    position: absolute;
    width: 530px;
    height: 303px;
    top: 296px;
    border-radius: 3px;
    box-shadow: 0 10px 28px rgba(0,0,0,.28);
    overflow: hidden;
  }
  .card--front { left: 50px; background: var(--card-white); color: var(--ink); }
  .card--back  { left: 620px; background: var(--card-black); }

  .wordmark {
    position: absolute;
    font-weight: 600;
    color: var(--gold);
    text-transform: uppercase;
    line-height: 1;
  }
  .wordmark__name { display: block; font-size: 25px; letter-spacing: 2px; }
  .wordmark__sub  { display: block; font-size: 15px; letter-spacing: 11px; margin-top: 5px; }
  .card--front .wordmark { left: 150px; top: 44px; }
  .card--back .wordmark { left: 0; right: 0; top: 126px; text-align: center; }

  .person { position: absolute; left: 110px; top: 112px; }
  .person__name { font-size: 17px; font-weight: 500; letter-spacing: 1px; text-transform: uppercase; }
  .person__title { font-size: 11px; letter-spacing: 1.5px; text-transform: uppercase; color: var(--ink-soft); margin-top: 2px; }

  .contact { position: absolute; list-style: none; font-size: 12px; letter-spacing: .4px; }
  .contact li { display: flex; align-items: flex-start; gap: 8px; margin-bottom: 6px; }
  .contact svg { flex: none; width: 12px; height: 12px; margin-top: 2px; fill: var(--ink); }
  .contact--location { left: 44px; top: 168px; }
  .contact--direct { left: 300px; top: 218px; }

  .accent-bars { position: absolute; left: 0; top: 0; width: 530px; height: 303px; }
</style>
</head>
<body>
  <section class="card card--front" aria-label="Card front">
    <svg class="accent-bars" viewBox="0 0 530 303" aria-hidden="true">
      <defs>
        <linearGradient id="goldBar" x1="0" x2="1">
          <stop offset="0" stop-color="#c9980f"/>
          <stop offset=".5" stop-color="#f0c53a"/>
          <stop offset="1" stop-color="#d8a716"/>
        </linearGradient>
      </defs>
      <rect x="34" y="236" width="248" height="8" fill="url(#goldBar)"/>
      <polygon points="282,236 290,236 298,285 290,285" fill="url(#goldBar)"/>
      <rect x="290" y="285" width="206" height="8" fill="url(#goldBar)"/>
    </svg>

    <div class="wordmark">
      <span class="wordmark__name">Peter Holloway</span>
      <span class="wordmark__sub">Interiors</span>
    </div>

    <div class="person">
      <p class="person__name">Evan Whitlock</p>
      <p class="person__title">General Manager</p>
    </div>

    <ul class="contact contact--location">
      <li>
        <svg viewBox="0 0 12 12"><path d="M6 0a4 4 0 0 0-4 4c0 3 4 8 4 8s4-5 4-8a4 4 0 0 0-4-4zm0 5.6A1.6 1.6 0 1 1 6 2.4a1.6 1.6 0 0 1 0 3.2z"/></svg>
        <span>27 North Brandel Street<br>Marsh Hollow NY 11492</span>
      </li>
      <li>
        <svg viewBox="0 0 12 12"><path d="M6 0a6 6 0 1 0 0 12A6 6 0 0 0 6 0zm0 1.2c.6.7 1.1 1.8 1.3 3.2H4.7C4.9 3 5.4 1.9 6 1.2zM1.3 6.8h2.2c0 1.3.3 2.4.7 3.3A4.8 4.8 0 0 1 1.3 6.8zm0-1.6a4.8 4.8 0 0 1 2.9-3.3c-.4.9-.7 2-.7 3.3zM6 10.8c-.6-.7-1.1-2.1-1.3-4h2.6c-.2 1.9-.7 3.3-1.3 4zm1.8-.7c.4-.9.7-2 .7-3.3h2.2a4.8 4.8 0 0 1-2.9 3.3zm.7-4.9c0-1.3-.3-2.4-.7-3.3a4.8 4.8 0 0 1 2.9 3.3z"/></svg>
        <span>www.phbwx.com</span>
      </li>
    </ul>

    <ul class="contact contact--direct">
      <li>
        <svg viewBox="0 0 12 12"><path d="M2.4 0l2 2.6-1.2 1.5a7 7 0 0 0 4.7 4.7l1.5-1.2L12 9.6 10.4 12C4.6 11.6.4 7.4 0 1.6z"/></svg>
        <span>718-555-0142</span>
      </li>
      <li>
        <svg viewBox="0 0 12 12"><path d="M3 0h6a1 1 0 0 1 1 1v10a1 1 0 0 1-1 1H3a1 1 0 0 1-1-1V1a1 1 0 0 1 1-1zm.4 1.4v8h5.2v-8zM6 9.9a.7.7 0 1 0 0 1.4.7.7 0 0 0 0-1.4z"/></svg>
        <span>646-555-0187</span>
      </li>
      <li>
        <svg viewBox="0 0 12 12"><path d="M0 2h12v8H0zm1.2 1.1v.3L6 6.6l4.8-3.2v-.3zm0 1.7v4h9.6v-4L6 8z"/></svg>
        <span>ph@phbwx.com</span>
      </li>
    </ul>
  </section>

  <section class="card card--back" aria-label="Card back">
    <div class="wordmark">
      <span class="wordmark__name">Peter Holloway</span>
      <span class="wordmark__sub">Interiors</span>
    </div>
  </section>
</body>
</html>
```